Stationary and Business Card for dental office
Velbrook Endodontics
Stationary and Business Card for dental office  - Health
Creative Brief
Use same font as used in my logo
use any font that is easy to read. should go with font in the logo
Professional
Miren T. Osbury, D.D.S.
418 Pelloway Court, Suite #1 Manteca, CA 95337
info@velbrookendo.example
www.velbrookendo.example
Business card should have 2 logos, one brown and gold one with a tooth image....that is my main logo. The second logo( the one that says pdrcertified member) which I have uploaded as well can be in a corner or anywhere on the card. basically it is your choice where it goes on the card. It does not have to be the same size as my main business logo. This second logo only needs to be on the business cards. it can be black and white or color. I will leave that decision to you so if you think the colored logo goes with my logo colors, then use that. If not then, use the black and white one. I will prefer it in color. Under my name on business card, please write the following in smaller font Practice Limited to Endodontics LETTER HEAD: deisgn does not need to have the second logo (pdrcertifeid member logo). It should have my main business logo ( gold and brown one) with business name and all the other info like address, phone, fax web/email. ENVELOPE: only main business logo with business name and address. Please do not include phone/fax/ email or any other logos on the envelope. Thank you.

```html
<!DOCTYPE html>
<html lang="en">
<head>
<meta charset="utf-8">
<title>Velbrook Endodontics — Stationery Set</title>
<link href="https://fonts.googleapis.com/css2?family=Lora:wght@500;600&family=Open+Sans:wght@400;600&display=swap" rel="stylesheet">
<style>
  :root{
    --bg:#eeeeee;
    --paper:#ffffff;
    --brown:#4e3320;
    --gold:#c79d5e;
    --gold-soft:#e6cfa6;
    --ink:#3a3a3a;
    --muted:#9a9a9a;
    --rule:#cfcfcf;
  }
  *{box-sizing:border-box;margin:0;padding:0}
  html,body{width:1200px;height:490px;overflow:hidden}
  body{background:var(--bg);font-family:"Open Sans",Arial,sans-serif;color:var(--ink);position:relative}
  .piece{position:absolute;background:var(--paper);box-shadow:0 2px 6px rgba(0,0,0,.12);overflow:hidden}
  .accent-band{position:absolute;left:0;width:100%;background:linear-gradient(180deg,rgba(199,157,94,.55),rgba(78,51,32,.35))}
  .brand{display:flex;align-items:center;gap:4px;position:absolute}
  .brand-dot{border-radius:50%;background:var(--gold);flex:none}
  .brand-name{font-family:"Lora",Georgia,serif;font-weight:600;color:var(--brown);white-space:nowrap}
  .tiny{font-size:4px;line-height:6px;color:var(--muted)}

  /* CD */
  .cd{left:24px;top:36px;width:132px;height:132px;border-radius:50%}
  .cd-hole{position:absolute;left:50%;top:50%;width:30px;height:30px;margin:-15px;border-radius:50%;background:var(--bg);border:6px solid #f4f4f4}
  .cd .brand{left:42px;top:22px}
  .cd .accent-band{top:100px;height:16px}

  /* business cards */
  .card{left:43px;width:113px;height:68px}
  .card-front{top:178px}
  .card-back{top:272px}
  .card-front .brand{left:14px;top:24px}
  .card-front .accent-band{bottom:0;height:10px}
  .card-back .brand{left:10px;top:10px}
  .card-name{position:absolute;left:10px;top:27px;font-family:"Lora",Georgia,serif;font-size:5px;color:var(--brown);font-weight:600}
  .card-role{position:absolute;left:10px;top:34px;font-size:4px;color:var(--gold)}
  .card-contact{position:absolute;left:10px;top:42px;width:95px}
  .badge{position:absolute;right:8px;top:8px;width:16px;height:16px;border-radius:50%;background:var(--gold-soft)}

  /* letterhead */
  .letterhead{left:180px;top:79px;width:175px;height:257px}
  .letterhead .brand{left:58px;top:22px}
  .letterhead .accent-band{bottom:34px;height:14px}
  .letter-body{position:absolute;left:18px;top:100px;width:120px}
  .letter-body p{margin-bottom:5px}
  .letter-foot{position:absolute;left:18px;bottom:8px;width:130px}

  /* envelope */
  .envelope{left:336px;top:221px;width:175px;height:91px;box-shadow:0 3px 8px rgba(0,0,0,.18)}
  .envelope .brand{left:10px;top:10px}
  .envelope .tiny{position:absolute;left:10px;top:22px}
  .envelope .accent-band{bottom:6px;height:12px}

  /* fax */
  .fax{left:533px;top:79px;width:180px;height:257px}
  .fax .brand{left:14px;top:16px}
  .fax-address{position:absolute;right:12px;top:14px;text-align:right;width:70px}
  .fax .accent-band{top:38px;height:10px}
  .fax-title{position:absolute;left:14px;top:64px;font-family:"Lora",Georgia,serif;font-size:20px;font-weight:600;color:var(--ink)}
  .fax-form{position:absolute;left:14px;top:94px;width:152px;display:grid;grid-template-columns:1fr 1fr;column-gap:8px}
  .fax-field{font-size:4px;color:var(--muted);border-bottom:0.6px solid var(--rule);padding:3px 0 1px}
  .fax-checks{position:absolute;left:14px;top:134px;display:flex;gap:6px}
  .fax-check{display:flex;align-items:center;gap:2px;font-size:3.5px;color:var(--muted)}
  .fax-check i{width:4px;height:4px;background:var(--brown);display:block}

  /* folder */
  .folder{left:804px;top:72px;width:204px;height:264px}
  .folder .accent-band{top:26px;height:14px}
  .folder-pocket{position:absolute;right:0;top:0;width:8px;height:100%;background:#c7a978}
  .folder-mark{position:absolute;left:111px;top:104px;width:48px;height:48px;border-radius:50%;background:var(--gold-soft)}
  .folder-address{position:absolute;left:110px;top:210px;width:80px}
</style>
</head>
<body>

<div class="piece cd">
  <div class="brand"><span class="brand-dot" style="width:6px;height:6px"></span><span class="brand-name" style="font-size:5px">Velbrook Endodontics</span></div>
  <div class="accent-band" role="img" aria-label="Brown and gold swoosh ornament"></div>
  <div class="cd-hole"></div>
</div>

<div class="piece card card-front">
  <div class="brand"><span class="brand-dot" style="width:9px;height:9px"></span><span class="brand-name" style="font-size:7px">Velbrook Endodontics</span></div>
  <div class="accent-band" role="img" aria-label="Brown and gold swoosh ornament"></div>
</div>

<div class="piece card card-back">
  <div class="brand"><span class="brand-dot" style="width:7px;height:7px"></span><span class="brand-name" style="font-size:5.5px">Velbrook Endodontics</span></div>
  <div class="badge"></div>
  <div class="card-name">Miren T. Osbury, D.D.S.</div>
  <div class="card-role">Practice Limited to Endodontics</div>
  <div class="card-contact tiny">418 Pelloway Court, Suite #1 Manteca, CA 95337<br>Phone (209) 555-0142<br>info@velbrookendo.example</div>
</div>

<div class="piece letterhead">
  <div class="brand"><span class="brand-dot" style="width:10px;height:10px"></span><span class="brand-name" style="font-size:7px">Velbrook Endodontics</span></div>
  <div class="letter-body tiny">
    <p>Thank you for choosing our practice for your endodontic care. We look forward to seeing you.</p>
    <p>Please arrive ten minutes early and bring your referral form and insurance card.</p>
  </div>
  <div class="accent-band" role="img" aria-label="Brown and gold swoosh ornament"></div>
  <div class="letter-foot tiny">418 Pelloway Court, Suite #1 Manteca, CA 95337<br>Phone (209) 555-0142 · Fax (209) 555-0143<br>info@velbrookendo.example · www.velbrookendo.example</div>
</div>

<div class="piece envelope">
  <div class="brand"><span class="brand-dot" style="width:8px;height:8px"></span><span class="brand-name" style="font-size:6px">Velbrook Endodontics</span></div>
  <div class="tiny">418 Pelloway Court, Suite #1<br>Manteca, CA 95337</div>
  <div class="accent-band" role="img" aria-label="Brown and gold swoosh ornament"></div>
</div>

<div class="piece fax">
  <div class="brand"><span class="brand-dot" style="width:8px;height:8px"></span><span class="brand-name" style="font-size:6px">Velbrook Endodontics</span></div>
  <div class="fax-address tiny">418 Pelloway Court, Suite #1 Manteca, CA 95337<br>www.velbrookendo.example</div>
  <div class="accent-band" role="img" aria-label="Brown and gold swoosh ornament"></div>
  <div class="fax-title">Fax</div>
  <div class="fax-form">
    <div class="fax-field">To</div><div class="fax-field">From</div>
    <div class="fax-field">Fax</div><div class="fax-field">Pages</div>
    <div class="fax-field">Phone</div><div class="fax-field">Date</div>
    <div class="fax-field">Re</div><div class="fax-field">CC</div>
  </div>
  <div class="fax-checks">
    <span class="fax-check"><i></i>Urgent</span>
    <span class="fax-check"><i></i>Review</span>
    <span class="fax-check"><i></i>Comment</span>
    <span class="fax-check"><i></i>Reply</span>
    <span class="fax-check"><i></i>Recycle</span>
  </div>
</div>

<div class="piece folder">
  <div class="accent-band" role="img" aria-label="Brown and gold swoosh ornament"></div>
  <div class="folder-mark" role="img" aria-label="Velbrook Endodontics mark"></div>
  <div class="folder-address tiny">418 Pelloway Court, Suite #1<br>Manteca, CA 95337<br>www.velbrookendo.example</div>
  <div class="folder-pocket"></div>
</div>

</body>
</html>
```